Website Re-design and extension of an existing website

I have a Wordpress website currently and I need it to be upgraded. I have MOST of the content to get it started and the rest (video's, pictures ect) are on the way. I want to know if it is possible to convert my existing website into a Personal Brand website with a public speaking emphasis. I would like to have my website modeled after the following website:

http://www.kvaltomira.example/

I have attached a document entitled "Website Outline & Content" that has all of the text on it and it has red headlines that indicate where something needs to be added or designed. I will be happy to give more detail if needed.

Things I still need to get to you in order to design the website;

-Demo video
-Full length public speaking video

Target Market(s)

Corporations, universities, trade associations, private events

Coding

Coded - Design and coding required

Requirements
Must have
• Pictures, links, downloadable forms, MULTIPLE video's embedded, my logo, keep the colors in sync with my existing marketing material
Nice to have
• I would like my design colors thematic as already inherent in my marketing materials (see my Speaker One Sheet)

```html
<!DOCTYPE html>
<html lang="en">
<head>
<meta charset="utf-8">
<title>Brant Oakley – Your Holistic Lifestyle Hacker</title>
<link href="https://fonts.googleapis.com/css2?family=Kaushan+Script&family=Lato:wght@300;400;700;900&family=Playfair+Display:wght@700;900&display=swap" rel="stylesheet">
<style>
:root{
  --olive:#a19c69;
  --olive-dark:#4b5531;
  --footer:#5c6238;
  --ink:#444;
  --muted:#666;
  --hero-top:#6f6f6f;
  --hero-bottom:#3a3a3a;
  --panel:#efefef;
  --dark:#1c1a12;
  --red:#e0493a;
  --teal:#5aaca7;
  --orange:#f4a11c;
  --white:#fff;
}
*{margin:0;padding:0;box-sizing:border-box}
html,body{width:842px;height:1200px;overflow:hidden}
body{position:relative;font-family:"Lato",sans-serif;color:var(--ink);background:var(--white)}
.abs{position:absolute}

/* header */
.site-header{left:0;top:0;width:842px;height:48px;background:var(--white)}
.brand{left:42px;top:10px;display:flex;align-items:center;gap:6px}
.brand-dot{width:26px;height:26px;border-radius:50%;background:var(--olive)}
.brand-name{font-family:"Lato",sans-serif;font-weight:900;font-size:15px;color:var(--olive);line-height:1}
.brand-tag{font-size:5px;letter-spacing:.5px;color:#333;text-transform:uppercase;margin-top:2px}
.main-nav{left:187px;top:18px;display:flex;gap:6px;font-size:7.6px;color:#555}
.main-nav .sep{color:var(--olive)}
.burger{left:800px;top:19px;width:11px}
.burger i{display:block;height:1.5px;background:#333;margin-bottom:2.5px}

/* hero */
.hero{left:0;top:48px;width:842px;height:329px;background:linear-gradient(180deg,var(--hero-top),#565656 55%,var(--hero-bottom))}
.hero-script{left:0;width:480px;top:86px;text-align:center;font-family:"Kaushan Script",cursive;font-size:25px;color:var(--white)}
.hero-title{left:114px;top:118px;display:flex;align-items:center;gap:9px;font-family:"Playfair Display",serif;font-weight:900;font-size:32px;color:var(--white)}
.hero-title span{background:var(--white);color:#222;padding:0 5px;line-height:34px}
.hero-sub{left:0;width:480px;top:163px;text-align:center;font-size:10px;color:var(--white)}
.hero-btn{left:173px;top:189px;width:134px;height:21px;background:var(--olive);color:#222;font-size:7.4px;font-weight:700;display:flex;align-items:center;justify-content:center;gap:6px}
.arrow-dot{width:10px;height:10px;border-radius:50%;background:#333;display:inline-flex;align-items:center;justify-content:center}
.sheet{width:110px;text-align:center;top:232px}
.sheet-ring{width:76px;height:76px;margin:0 auto;border:1px dashed rgba(255,255,255,.7);border-radius:50%;display:flex;align-items:center;justify-content:center}
.sheet-core{width:66px;height:66px;border-radius:50%;display:flex;align-items:center;justify-content:center}
.sheet-label{font-size:8.6px;color:var(--white);margin-top:12px}

/* about */
.about{left:0;top:377px;width:842px;height:328px;background:linear-gradient(180deg,#f7f7f7,var(--panel))}
.desk-items{left:0;top:380px;width:200px;height:320px;background:linear-gradient(135deg,#e4e4e4,#d4d4d4 60%,#ececec)}
.tabs{left:122px;top:393px;display:flex;align-items:center;gap:11px;font-size:6.8px;color:#444}
.tab-active{background:var(--olive);color:var(--white);padding:5px 9px;position:relative}
.tab-active::after{content:"";position:absolute;left:50%;bottom:-4px;margin-left:-4px;border:4px solid transparent;border-bottom:0;border-top-color:var(--olive)}
.about-title{left:230px;width:224px;top:429px;text-align:right;font-size:19px;font-weight:300;color:#555}
.about-text{left:114px;width:340px;top:470px;text-align:right;font-size:7.2px;line-height:13.7px;color:var(--muted)}
.read-more{left:374px;top:598px;width:79px;height:24px;background:var(--olive-dark);color:var(--white);font-size:7.2px;font-weight:700;letter-spacing:.4px;display:flex;align-items:center;justify-content:center;gap:7px}
.read-more .arrow-dot{background:var(--white)}
.laptop{left:478px;top:340px;width:364px;height:310px;background:#cfd1d3;border-radius:12px 0 0 0}
.laptop-screen{left:503px;top:364px;width:339px;height:257px;background:linear-gradient(135deg,#5a4a3c,#c9a77b 45%,#8d6c4f)}
.laptop-base{left:468px;top:650px;width:374px;height:9px;background:linear-gradient(180deg,#d9d9d9,#a8a8a8);border-radius:0 0 0 8px}

/* testimonials */
.testimonials{left:0;top:705px;width:842px;height:235px;background:radial-gradient(ellipse at 30% 40%,#4a3a20,var(--dark) 70%)}
.t-kicker{left:0;width:618px;top:749px;text-align:center;font-size:8.4px;color:var(--white)}
.t-title{left:0;width:618px;top:762px;text-align:center;font-size:16px;font-weight:700;color:var(--white)}
.t-quote{left:114px;width:390px;top:810px;text-align:center;font-size:6.4px;line-height:11.6px;color:var(--white)}
.t-cite{left:0;width:618px;top:894px;text-align:center;font-size:7.6px;color:var(--white)}
.t-arrow{top:834px}
.t-faces{left:630px;top:705px}

/* partners */
.partners{left:0;top:940px;width:842px;height:37px;background:#fafafa}
.partner{top:951px;height:14px;background:#cfcfcf;border-radius:2px}

/* footer */
.site-footer{left:0;top:977px;width:842px;height:223px;background:var(--footer)}
.f-brand{left:0;width:842px;top:996px;text-align:center;color:var(--white)}
.f-dot{width:44px;height:44px;border-radius:50%;background:var(--white);margin:0 auto 6px}
.f-name{font-weight:900;font-size:19px;line-height:1}
.f-tag{font-size:5px;letter-spacing:.6px;text-transform:uppercase;margin-top:3px}
.signup{left:247px;top:1085px;width:348px;height:22px;display:flex}
.signup-field{flex:1;background:var(--white);font-size:6.4px;color:#888;padding-left:10px;display:flex;align-items:center}
.signup-btn{width:51px;background:var(--olive);color:var(--white);font-size:6.4px;font-weight:700;display:flex;align-items:center;justify-content:center}
.f-rule{left:401px;top:1118px;width:40px;height:1px;background:rgba(255,255,255,.7)}
.socials{left:377px;top:1138px;display:flex;gap:9px}
.socials i{width:6px;height:6px;border-radius:50%;background:var(--olive)}
.f-nav{left:0;width:842px;top:1159px;text-align:center;font-size:7.2px;color:var(--white)}
.f-nav span{margin:0 4px;opacity:.8}
.f-copy{left:0;width:842px;top:1173px;text-align:center;font-size:6.6px;color:var(--white)}
.to-top{left:762px;top:1159px}
</style>
</head>
<body>

<header class="abs site-header">
  <div class="abs brand">
    <div class="brand-dot"></div>
    <div>
      <div class="brand-name">BRANT OAKLEY</div>
      <div class="brand-tag">Your holistic lifestyle hacker</div>
    </div>
  </div>
  <nav class="abs main-nav">
    <a>Home</a><span class="sep">::</span><a>About us</a><span class="sep">::</span><a>Motivational Speaker/Keynote</a><span class="sep">::</span><a>Workshop Presenter</a><span class="sep">::</span><a>Author</a><span class="sep">::</span><a>Coaching</a><span class="sep">::</span><a>Blog</a><span class="sep">::</span><a>Online Courses</a><span class="sep">::</span><a>Contact Brant Oakley</a>
  </nav>
  <div class="abs burger"><i></i><i></i><i></i></div>
</header>

<section class="abs hero" role="img" aria-label="Photo of the speaker smiling, leaning on a wooden fence with mountains behind"></section>
<div class="abs hero-script">Your Holistic</div>
<h1 class="abs hero-title">Lifestyle <span>Hacker</span></h1>
<p class="abs hero-sub">Lose Your Mind &amp; Find Your Health!</p>
<a class="abs hero-btn">See How Brant Oakley Can Help <span class="arrow-dot"><svg width="6" height="6" viewBox="0 0 6 6"><path d="M1 3h4M3 1l2 2-2 2" stroke="#fff" stroke-width="1" fill="none"/></svg></span></a>

<div class="abs sheet" style="left:62px">
  <div class="sheet-ring"><div class="sheet-core" style="background:var(--red)">
    <svg width="30" height="26" viewBox="0 0 30 26" fill="none" stroke="#fff" stroke-width="2"><path d="M4 9h5l12-6v20L9 17H4z"/><path d="M9 17l2 7h4l-2-6"/><path d="M24 9v8"/></svg>
  </div></div>
  <div class="sheet-label">Brant's Speaker One Sheet</div>
</div>
<div class="abs sheet" style="left:183px">
  <div class="sheet-ring"><div class="sheet-core" style="background:var(--teal)">
    <svg width="32" height="32" viewBox="0 0 32 32" fill="none" stroke="#fff" stroke-width="2"><circle cx="23" cy="7" r="4"/><circle cx="8" cy="16" r="4"/><circle cx="23" cy="25" r="4"/><path d="M12 14l7-5M12 18l7 5"/></svg>
  </div></div>
  <div class="sheet-label">Brant's Media Sheet</div>
</div>
<div class="abs sheet" style="left:302px">
  <div class="sheet-ring"><div class="sheet-core" style="background:var(--orange)">
    <svg width="24" height="32" viewBox="0 0 24 32" fill="none" stroke="#fff" stroke-width="2"><rect x="7" y="2" width="10" height="17" rx="5"/><path d="M3 14a9 9 0 0 0 18 0M12 23v5M7 29h10"/></svg>
  </div></div>
  <div class="sheet-label">Brant's College Speaker One Sheet</div>
</div>

<section class="abs about"></section>
<div class="abs desk-items" role="img" aria-label="Keyboard, mouse and earphones on a desk"></div>
<div class="abs laptop"></div>
<div class="abs laptop-screen" role="img" aria-label="Childhood photo of kids holding rabbits"></div>
<div class="abs laptop-base"></div>
<div class="abs tabs">
  <span class="tab-active">Brant Oakley</span><span>|</span><span>Sugar Addiction Expert</span><span>|</span><span>Holistic Health Expert</span><span>|</span><span>Author &amp; Speaker</span>
</div>
<h2 class="abs about-title">About Brant Oakley</h2>
<p class="abs about-text">For over 17 years, Brant Oakley has tirelessly helped executives, employees, and everyday people achieve lasting health and fitness by helping them “lose their minds.” Using his unique 4-Quadrant Coaching System, speaking platform, and online training courses, Brant has helped hundreds of people shed their limiting beliefs, eat better, shed sugar addiction and transform their bodies and minds. Brant delights in helping people see through the self-deception of being “normal,” and he invites his students to discover and accept the extraordinary people they truly are. If you are ready to transform physically, mentally, emotionally, and spiritually, it is time for you to meet Brant Oakley, your Holistic Health Hacker!</p>
<a class="abs read-more">READ MORE <span class="arrow-dot"><svg width="6" height="6" viewBox="0 0 6 6"><path d="M1 3h4M3 1l2 2-2 2" stroke="#333" stroke-width="1" fill="none"/></svg></span></a>

<section class="abs testimonials"></section>
<p class="abs t-kicker">what others say about</p>
<h2 class="abs t-title">Testimonials</h2>
<p class="abs t-quote">"An important aspect of a successful and highly effective workforce is good health. Brant Oakley of Evergreen Vitality provides a wealth of knowledge trough his CoreFit and Sugar Addiction Courses that has visibly changed the lives of many of the executives at Ridgeline Federal. He brought a whole new level of understanding on good nutrition and the pitfalls of certain poor food choices. But that is just the beginning of the training. Brant has trained the staff on good sleep habits, stress management, and exercise. All of this has been combined with individual one-on-one training with staff and their spouses. The individual coaching is flexible and targeted on areas that will most benefit the participants"</p>
<p class="abs t-cite">-Dorian Vance, CEO Ridgeline Federal Credit Union</p>
<svg class="abs t-arrow" style="left:68px" width="10" height="16" viewBox="0 0 10 16"><path d="M8 2L2 8l6 6" stroke="#fff" stroke-width="2" fill="none"/></svg>
<svg class="abs t-arrow" style="left:544px" width="10" height="16" viewBox="0 0 10 16"><path d="M2 2l6 6-6 6" stroke="#fff" stroke-width="2" fill="none"/></svg>
<svg class="abs t-faces" width="212" height="235" viewBox="0 0 212 235">
  <polygon points="52,0 212,0 212,235 3,235" fill="#fff"/>
  <polygon points="44,2 208,2 195,77 24,77" fill="#b9bdc2" role="img" aria-label="Portrait of a smiling businessman"/>
  <polygon points="23,80 192,80 177,153 10,153" fill="#9a9a9a" role="img" aria-label="Portrait of a businessman with glasses"/>
  <polygon points="9,156 176,156 160,232 0,232" fill="#c6c3c6" role="img" aria-label="Portrait of a businessman in a purple shirt"/>
</svg>

<section class="abs partners" aria-label="Partner organizations"></section>
<div class="abs partner" style="left:78px;width:58px"></div>
<div class="abs partner" style="left:186px;width:16px"></div>
<div class="abs partner" style="left:254px;width:58px"></div>
<div class="abs partner" style="left:360px;width:18px"></div>
<div class="abs partner" style="left:452px;width:14px;border-radius:50%"></div>
<div class="abs partner" style="left:538px;width:24px"></div>
<div class="abs partner" style="left:626px;width:46px"></div>
<div class="abs partner" style="left:724px;width:40px"></div>

<footer class="abs site-footer"></footer>
<div class="abs f-brand">
  <div class="f-dot"></div>
  <div class="f-name">BRANT OAKLEY</div>
  <div class="f-tag">Your holistic lifestyle hacker</div>
</div>
<form class="abs signup">
  <div class="signup-field">Get Brant Oakley Branding Secrets Now</div>
  <div class="signup-btn">SUBSCRIBE</div>
</form>
<div class="abs f-rule"></div>
<div class="abs socials"><i></i><i></i><i></i><i></i><i></i><i></i></div>
<nav class="abs f-nav">Home<span>|</span>About us<span>|</span>Motivational Speaker/Keynote<span>|</span>Workshop Presenter<span>|</span>Author<span>|</span>Coaching<span>|</span>Blog<span>|</span>Online Courses<span>|</span>Contact Brant Oakley</nav>
<p class="abs f-copy">© Copyright 2017 &nbsp;Privacy Policy &nbsp;:: &nbsp;Terms of Use &nbsp;:: &nbsp;Cookies Policy</p>
<svg class="abs to-top" width="28" height="28" viewBox="0 0 28 28"><circle cx="14" cy="14" r="13" fill="#fff"/><path d="M14 21V8M8 13l6-6 6 6" stroke="var(--footer)" stroke-width="3" fill="none"/></svg>

</body>
</html>
```